Spannish marketing agency needs redesign of powerpoint presentation for client acquisition

We want to redesign our powerpoint presentation. We use this presentation to show our clients how we work. WE NEED IT TO BE IN POWERPOINT FORMAT
The style should match the style of our logo and story brand, but apart from that we want designers to get creative.
Updates
The project must be in powerpoint format. The project must be in powerpoint format
Baja calidad de diseño
Target Market(s)
Small and medium size business owners
Industry/Entity Type
Digital marketing
Look and feel
Each slider illustrates characteristics of the customer's brand and the style your logo design should communicate.

```html
<!DOCTYPE html>
<html lang="es">
<head>
<meta charset="utf-8">
<title>Velaria · 5 pasos para tu plan estratégico de marketing</title>
<link rel="stylesheet" href="https://fonts.googleapis.com/css2?family=Montserrat:wght@400;500;600&display=swap">
<style>
  :root {
    --board: #808080;
    --paper: #ffffff;
    --ink: #111111;
    --navy: #0b1a3a;
    --brand: #0a64d2;
    --brand-soft: #6fa6e6;
    --brand-pale: #d8e7f8;
  }
  * { margin: 0; padding: 0; box-sizing: border-box; }
  html, body { width: 1200px; height: 675px; overflow: hidden; background: var(--board); }
  body { position: relative; font-family: "Montserrat", Arial, sans-serif; color: var(--ink); }

  .slide {
    position: absolute;
    width: 489px; height: 275px;
    background: var(--paper);
    overflow: hidden;
  }
  .slide--cover   { left: 60px;  top: 34px; }
  .slide--index   { left: 651px; top: 34px; }
  .slide--intro   { left: 60px;  top: 366px; }
  .slide--context { left: 651px; top: 366px; }

  .slide__art { position: absolute; left: 0; top: 0; width: 489px; height: 275px; }

  .brand-name {
    position: absolute;
    font-weight: 500;
    color: var(--navy);
    letter-spacing: 0.14em;
  }

  /* Cover */
  .cover__title {
    position: absolute; left: 28px; top: 40px;
    font-size: 14px; font-weight: 500; line-height: 17.5px;
    letter-spacing: 0.02em; text-transform: uppercase;
  }
  .slide--cover .brand-name { left: 285px; top: 42px; font-size: 28px; }

  /* Index */
  .steps { position: absolute; left: 77px; top: 36px; list-style: none; }
  .steps__item { display: flex; font-size: 11px; font-weight: 500; line-height: 19.5px; letter-spacing: 0.02em; }
  .steps__num { width: 55px; color: var(--ink); }
  .steps__name { color: var(--brand); }
  .slide--index .brand-name { left: 388px; top: 224px; font-size: 12.5px; }

  /* Text slides */
  .copy {
    position: absolute; left: 47px; width: 397px;
    font-size: 6.2px; line-height: 8.65px; text-align: justify;
  }
  .copy p + p { margin-top: 0; }
  .copy .gap { margin-top: 8.6px; }
  .copy ul { list-style: none; }
  .copy li { padding-left: 7px; text-indent: -7px; }
  .intro__heading {
    position: absolute; left: 47px; top: 33px;
    font-size: 11px; font-weight: 500; line-height: 13px;
    color: var(--brand); letter-spacing: 0.01em;
  }
  .slide--intro .copy { top: 69px; }
  .slide--intro .copy li { line-height: 10px; text-align: left; }
  .slide--context .copy { top: 44px; }
  .highlight { color: var(--brand); }
</style>
</head>
<body>

  <!-- Cover -->
  <section class="slide slide--cover">
    <svg class="slide__art" viewBox="0 0 489 275" aria-hidden="true">
      <defs>
        <linearGradient id="cover-plane" x1="0" y1="1" x2="1" y2="0">
          <stop offset="0" stop-color="#6fa6e6"/>
          <stop offset="1" stop-color="#0a64d2"/>
        </linearGradient>
        <radialGradient id="cover-glow" cx="0.35" cy="1" r="0.8">
          <stop offset="0" stop-color="#2f7fdc"/>
          <stop offset="1" stop-color="#d8e7f8"/>
        </radialGradient>
      </defs>
      <ellipse cx="110" cy="290" rx="140" ry="80" fill="url(#cover-glow)" opacity="0.9"/>
      <polygon points="0,250 489,150 489,275 0,275" fill="url(#cover-plane)" opacity="0.85"/>
      <polygon points="0,250 489,150 489,156 0,256" fill="#0a64d2"/>
    </svg>
    <h1 class="cover__title">5 pasos para desarrollar<br>tu plan estratégico de<br>marketing</h1>
    <div class="brand-name">VELARIA</div>
  </section>

  <!-- Index -->
  <section class="slide slide--index">
    <svg class="slide__art" viewBox="0 0 489 275" aria-hidden="true">
      <defs>
        <linearGradient id="index-plane" x1="0" y1="0" x2="1" y2="1">
          <stop offset="0" stop-color="#9cc2ee"/>
          <stop offset="1" stop-color="#0a64d2"/>
        </linearGradient>
      </defs>
      <polygon points="0,196 300,275 0,275" fill="url(#index-plane)" opacity="0.8"/>
      <polygon points="0,194 300,275 292,275 0,200" fill="#0a64d2"/>
    </svg>
    <ol class="steps">
      <li class="steps__item"><span class="steps__num">PASO 1.</span><span class="steps__name">ANÁLISIS INICIAL</span></li>
      <li class="steps__item"><span class="steps__num">PASO 2.</span><span class="steps__name">IDENTIDAD DE MARCA</span></li>
      <li class="steps__item"><span class="steps__num">PASO 3.</span><span class="steps__name">OBJETIVOS DE NUESTRA EMPRESA</span></li>
      <li class="steps__item"><span class="steps__num">PASO 4.</span><span class="steps__name">RECORRIDO DEL COMPRADOR</span></li>
      <li class="steps__item"><span class="steps__num">PASO 5.</span><span class="steps__name">DEFINIR EQUIPO DE PROFESIONALES NECESARIO</span></li>
    </ol>
    <div class="brand-name">VELARIA</div>
  </section>

  <!-- Intro -->
  <section class="slide slide--intro">
    <svg class="slide__art" viewBox="0 0 489 275" aria-hidden="true">
      <defs>
        <linearGradient id="foot-glow" x1="0" y1="0" x2="1" y2="0">
          <stop offset="0" stop-color="#d8e7f8"/>
          <stop offset="1" stop-color="#6fa6e6"/>
        </linearGradient>
      </defs>
      <ellipse cx="190" cy="280" rx="70" ry="14" fill="url(#foot-glow)"/>
      <rect x="0" y="269" width="30" height="6" fill="#0a64d2"/>
      <rect x="45" y="269" width="7" height="6" fill="#0a64d2"/>
      <rect x="438" y="269" width="30" height="6" fill="#0a64d2"/>
      <rect x="482" y="269" width="7" height="6" fill="#0a64d2"/>
    </svg>
    <h2 class="intro__heading">¿POR QUÉ MUCHAS EMPRESAS PIERDEN<br>DINERO AL INICIARSE EN EL MARKETING DIGITAL?</h2>
    <div class="copy">
      <p>En los últimos años el marketing digital ha ido ganando fuerza a la hora de facilitar a las empresas captar y fidelizar clientes. Hay empresas que se han adaptado rápidamente y han logrado muy buenos resultados, otras que han ido adaptándose poco a poco y por último hay un grupo de empresas que no consideraba necesario utilizar estas herramientas, ya que su negocio funcionaba bien captando clientes de forma tradicional.</p>
      <p>Sin embargo ha ocurrido una situación que nadie podía esperar. La pandemia ha acelerado la velocidad a la que las empresas han tenido que adaptarse a la captación y el manejo de clientes en los medios digitales. Muchos empresarios se han visto obligados a familiarizarse con un gran número de nuevos términos como SEO, SEM, creación de contenido, community manager, facebook ads, email marketing, crm en un periodo de tiempo extremadamente corto.</p>
      <p class="gap">Esta situación ha llevado a la necesidad de un nuevo proceso de toma de decisiones, estos pensamientos incluyen:</p>
      <ul>
        <li>- Tenemos que actualizar nuestra página web</li>
        <li>- Hay que contratar a alguien para que nos maneje instagram y facebook</li>
        <li>- Tenemos que poner anuncios para que la gente vea nuestros productos.</li>
        <li>- Hay que buscar una manera digital de mantener la relación con los clientes</li>
      </ul>
    </div>
  </section>

  <!-- Context -->
  <section class="slide slide--context">
    <svg class="slide__art" viewBox="0 0 489 275" aria-hidden="true">
      <ellipse cx="220" cy="280" rx="70" ry="14" fill="url(#foot-glow)"/>
      <rect x="0" y="269" width="30" height="6" fill="#0a64d2"/>
      <rect x="45" y="269" width="7" height="6" fill="#0a64d2"/>
      <rect x="310" y="269" width="105" height="6" fill="#0a64d2"/>
      <rect x="438" y="269" width="30" height="6" fill="#0a64d2"/>
      <rect x="482" y="269" width="7" height="6" fill="#0a64d2"/>
    </svg>
    <div class="copy">
      <p>Este tipo de acciones de por si no tienen nada malo, sin embargo una ejecución descoordinada de ellas sin un rumbo fijo puede llevar a consecuencias muy negativas. Algunas de las frases más habituales que solemos escuchar en nuestra agencia son:</p>
      <ul>
        <li>- &nbsp;Hemos invertido 3000 euros en que nos hagan una página web nueva pero no la visita casi nadie</li>
        <li>- &nbsp;He promocionado mis productos en facebook y no he conseguido vender nada</li>
        <li>- &nbsp;Los clientes habituales dicen que la imagen que proyectamos en las redes sociales no tiene nada que ver con lo que es nuestra empresa</li>
      </ul>
      <p class="gap">Esto lleva a pensar a muchos empresarios que realmente el marketing digital no funciona y que es una pérdida de tiempo y dinero. Este pensamiento es completamente comprensible y además se ve reforzado por un bombardeo continuo de publicidad por parte de un sector con titulares tan impactantes "la herramienta definitiva de marketing", "el método seguro para hacer tu negocio crecer", "el método de SEO que multiplicará tus visitas",</p>
      <p>Sin embargo, son miles los ejemplos de empresas que utilizan el marketing digital de forma eficiente y que aumentan continuamente su número de clientes. Uno de los factores comunes que tienen estas empresas es que sus acciones están coordinadas y son coherentes con sus objetivos.</p>
      <p>Para ayudarte a aprovechar las grandes posibilidades que nos aportan los medios digitales te vamos a enseñar los 5 pasos que puedes usar para desarrollar tu <span class="highlight">PLAN ESTRATEGICO DE MARKETING DIGITAL</span>.</p>
    </div>
  </section>

</body>
</html>
```